Customs House descriptive business cards

We require a two-sided business card that has a simple yet elegant design. We want to be able to promote our services as a customs house. This card should include our logo, contact info and services offered with the logo being on one side and the contact info and services on the flip side

Target Market(s)

Importers / exporters to and from the Bahamas

Industry/Entity Type

Logistics

Contact Information for Business Card

The front side of the card could have the logo and the flip side should have the other relevant info

Font styles to use
Serif

Colors

Designer to choose colors to be used in the design.

Requirements
Must have
• (Harbourline Agents Ltd) Logo, address and contact info also services:
• import customs clearance, Delivery & HAndling services,Florida pickups, Export packing & Crating Services, export customs clearance, Consulting

```html
<!DOCTYPE html>
<html lang="en">
<head>
<meta charset="utf-8">
<title>Harbourline Agents Ltd — Business Card</title>
<link rel="stylesheet" href="https://fonts.googleapis.com/css2?family=Cormorant+Garamond:wght@400;600&family=PT+Sans:wght@400&display=swap">
<style>
  :root {
    --stage-light: #a9a9a9;
    --stage-dark: #5b5b5b;
    --card-black: #0d0d0e;
    --card-edge: #1a1a1c;
    --brand-blue: #2a8ad6;
    --text-light: #d9d9d9;
    --text-muted: #bdbdbd;
    --band-grey: #d6d6d6;
  }
  * { margin: 0; padding: 0; box-sizing: border-box; }
  html, body { width: 1200px; height: 900px; overflow: hidden; }
  body {
    background: radial-gradient(ellipse at 50% 35%, var(--stage-light) 0%, var(--stage-dark) 100%);
    font-family: "PT Sans", sans-serif;
    position: relative;
  }
  .card {
    position: absolute;
    left: 285px;
    width: 630px;
    height: 360px;
    border-radius: 24px;
    background: var(--card-black);
    border: 1px solid var(--card-edge);
    box-shadow: 0 18px 40px rgba(0,0,0,0.45);
    overflow: hidden;
  }
  .card--front { top: 60px; }
  .card--back { top: 480px; }

  /* Front */
  .front-mark {
    position: absolute;
    inset: 0;
    display: flex;
    align-items: center;
    justify-content: center;
    gap: 14px;
  }
  .mark-dot {
    width: 16px; height: 16px;
    border-radius: 50%;
    background: var(--brand-blue);
  }
  .company-name {
    font-family: "Cormorant Garamond", serif;
    font-weight: 600;
    color: var(--brand-blue);
    letter-spacing: 1px;
  }
  .front-mark .company-name { font-size: 40px; }

  /* Back */
  .back-mark {
    position: absolute;
    left: 40px; top: 34px;
    display: flex; align-items: center; gap: 10px;
  }
  .back-mark .mark-dot { width: 11px; height: 11px; }
  .back-mark .company-name { font-size: 21px; }

  .person-name {
    position: absolute;
    left: 40px; top: 108px;
    font-family: "Cormorant Garamond", serif;
    font-weight: 400;
    font-size: 30px;
    letter-spacing: 2px;
    color: var(--text-muted);
  }
  .job-title {
    position: absolute;
    left: 40px; top: 150px;
    font-size: 12px;
    letter-spacing: 0.5px;
    color: var(--brand-blue);
  }
  .divider {
    position: absolute;
    left: 112px; right: 0; top: 161px;
    height: 2px;
    background: var(--brand-blue);
  }
  .contact-list {
    position: absolute;
    left: 40px; top: 188px;
    list-style: none;
  }
  .contact-list li {
    display: flex; align-items: center; gap: 10px;
    font-size: 15px;
    color: var(--text-light);
    height: 24px;
  }
  .contact-list svg { width: 14px; height: 14px; fill: var(--brand-blue); flex: none; }

  .service-list {
    position: absolute;
    right: 38px; top: 24px;
    list-style: none;
    text-align: right;
  }
  .service-list li {
    font-size: 16px;
    line-height: 21px;
    color: var(--text-light);
  }
  .service-list li::after {
    content: "";
    display: inline-block;
    width: 6px; height: 6px;
    margin-left: 8px;
    border-radius: 50%;
    background: var(--brand-blue);
    vertical-align: middle;
  }
  .bottom-band {
    position: absolute;
    left: 0; right: 0; bottom: 0;
    height: 34px;
    display: flex;
  }
  .bottom-band__blue { flex: 0 0 64%; background: var(--brand-blue); }
  .bottom-band__grey { flex: 1; background: var(--band-grey); }
</style>
</head>
<body>

  <section class="card card--front" aria-label="Card front">
    <div class="front-mark">
      <span class="mark-dot"></span>
      <span class="company-name">Harbourline Agents Ltd</span>
    </div>
  </section>

  <section class="card card--back" aria-label="Card back">
    <div class="back-mark">
      <span class="mark-dot"></span>
      <span class="company-name">Harbourline Agents Ltd</span>
    </div>

    <h1 class="person-name">YOUR NAME</h1>
    <p class="job-title">JOB TITLE</p>
    <div class="divider"></div>

    <ul class="contact-list">
      <li>
        <svg viewBox="0 0 24 24" aria-hidden="true"><path d="M6.6 10.8a15 15 0 0 0 6.6 6.6l2.2-2.2a1 1 0 0 1 1-.25 11.4 11.4 0 0 0 3.6.57 1 1 0 0 1 1 1V20a1 1 0 0 1-1 1A17 17 0 0 1 3 4a1 1 0 0 1 1-1h3.5a1 1 0 0 1 1 1c0 1.25.2 2.45.57 3.57a1 1 0 0 1-.25 1z"/></svg>
        000 000 0000
      </li>
      <li>
        <svg viewBox="0 0 24 24" aria-hidden="true"><path d="M3 5h18v14H3zm2 2v.5l7 4.5 7-4.5V7zm0 2.9V17h14V9.9l-7 4.5z"/></svg>
        youremail@xyz.com
      </li>
      <li>
        <svg viewBox="0 0 24 24" aria-hidden="true"><path d="M12 2a7 7 0 0 0-7 7c0 5 7 13 7 13s7-8 7-13a7 7 0 0 0-7-7zm0 9.5A2.5 2.5 0 1 1 12 6.5a2.5 2.5 0 0 1 0 5z"/></svg>
        youraddresshere
      </li>
    </ul>

    <ul class="service-list">
      <li>Import Customs Clearance</li>
      <li>Delivery &amp; Handling Services</li>
      <li>Florida pickups</li>
      <li>Export packing &amp; Crating Services</li>
      <li>Export Customs Clearance</li>
      <li>Consulting</li>
    </ul>

    <div class="bottom-band">
      <div class="bottom-band__blue"></div>
      <div class="bottom-band__grey"></div>
    </div>
  </section>

</body>
</html>
```